New (old) Business Card Design Project

I would like to purchase a customized version of a design you have previously submitted - https://www.artmarketly.example/design/7305126

I like the card above, and would like to use the same design, jus with my business name, HARLOWAY ASSET ADVISORS. I like the colors in the card above, as well as the font. The other side will have my name, company name, address, phone, email, website, plus disclosure text I will provide.

Target Market(s)

wealthy families

Industry/Entity Type

Financial Services

Contact Information for Business Card

logo on one side, on other my name, company, address, phone, email, website, disclosure language I will provide.

Colors

Designer to choose colors to be used in the design.

Requirements
Must have
• colors: Deep blue and white
Nice to have
• Please see the items I have uploaded, below.
Should not have
• Cheap, tacky look.

```html
<!DOCTYPE html>
<html lang="en">
<head>
<meta charset="utf-8">
<title>Harloway Asset Advisors — Business Card</title>
<link href="https://fonts.googleapis.com/css2?family=Cinzel:wght@400&family=Montserrat:wght@500;600&family=Arimo:wght@400&display=swap" rel="stylesheet">
<style>
  :root {
    --navy: #0b2163;
    --navy-deep: #081a52;
    --white: #ffffff;
    --ink: #2a2a2a;
    --backdrop: #e7eaeb;
  }
  * { box-sizing: border-box; margin: 0; padding: 0; }
  html, body { width: 1200px; height: 900px; overflow: hidden; }
  body {
    background: var(--backdrop);
    display: flex;
    align-items: center;
    justify-content: center;
    gap: 40px;
  }
  .card {
    width: 520px;
    height: 297px;
    position: relative;
    overflow: hidden;
    box-shadow: 0 2px 6px rgba(0,0,0,0.12);
    background: var(--white);
  }

  /* Front */
  .front-field {
    position: absolute; left: 0; top: 0; right: 0; height: 236px;
    background: linear-gradient(160deg, var(--navy) 0%, var(--navy) 60%, var(--navy-deep) 100%);
    display: flex; align-items: center; justify-content: center;
  }
  .brand-name {
    font-family: "Cinzel", serif;
    font-weight: 400;
    font-size: 27px;
    letter-spacing: 0.07em;
    color: var(--white);
    white-space: nowrap;
  }
  .tagline {
    position: absolute; left: 0; right: 0; top: 236px; height: 52px;
    display: flex; align-items: center; justify-content: center; gap: 22px;
    font-family: "Cinzel", serif;
    font-size: 16px;
    letter-spacing: 0.06em;
    color: var(--navy);
  }
  .tagline .sep { width: 1px; height: 14px; background: var(--navy); }
  .front-rule {
    position: absolute; left: 0; right: 0; bottom: 3px; height: 4px;
    background: var(--navy);
  }

  /* Back */
  .identity {
    position: absolute; right: 276px; top: 127px;
    text-align: right;
  }
  .person-name {
    font-family: "Montserrat", sans-serif;
    font-weight: 600;
    font-size: 21px;
    letter-spacing: 0.02em;
    color: var(--navy);
    line-height: 1;
    white-space: nowrap;
  }
  .person-title {
    font-family: "Montserrat", sans-serif;
    font-weight: 500;
    font-size: 10px;
    letter-spacing: 0.08em;
    color: var(--navy-deep);
    margin-top: 4px;
  }
  .divider {
    position: absolute; left: 262px; top: 86px;
    width: 1.5px; height: 126px; background: var(--navy);
  }
  .contact {
    position: absolute; left: 282px; top: 90px;
    font-family: "Arimo", sans-serif;
    font-size: 12px;
    line-height: 1.4;
    color: var(--ink);
    white-space: nowrap;
  }
  .contact .address { margin-bottom: 12px; }
  .contact .label { color: var(--navy); }
</style>
</head>
<body>
  <section class="card card-front" aria-label="Card front">
    <div class="front-field">
      <span class="brand-name">HARLOWAY ASSET ADVISORS</span>
    </div>
    <div class="tagline">
      <span>Plan</span><span class="sep"></span>
      <span>Preserve</span><span class="sep"></span>
      <span>Provide</span>
    </div>
    <div class="front-rule"></div>
  </section>

  <section class="card card-back" aria-label="Card back">
    <div class="identity">
      <div class="person-name">MAREN OSTLUND</div>
      <div class="person-title">DIRECTOR</div>
    </div>
    <div class="divider"></div>
    <div class="contact">
      <p class="address">418 Corrin Lane<br>Halden Ridge 20481</p>
      <p><span class="label">phone:</span> 555 014 2736</p>
      <p><span class="label">e-mail:</span> contact@harloway.example</p>
      <p><span class="label">website:</span> www.harloway.example</p>
    </div>
  </section>
</body>
</html>
```